Visitenkarten-Design für Stillberaterin
Zielgruppe
Ich bin Stillberaterin ZMRPT, d. h. ich berate Mütter bei Stillschwierigkeiten. Meine Zielgruppe sind junge Familien, die sich vorab über das Stillen Ihres Kindes informieren möchten, Stillschwierigkeiten (z. B. Schmerzen, schlechte Gewichtszunahme usw.) haben oder Fragen rund ums Stillen haben (Medikamente, Stillen in besonderen Situationen...). Weiterhin biete ich Kurse für den Beikoststart oder zum Abstillen an.
Aufgabenstellung
Auf meiner Visitenkarte sollte mein Logo sowie alle Kontaktdaten klar und deutlich erkennbar sein. Die Farben sind dem Logo anzupassen. Die Schriftarten, die im Logo verwendet werden sind: Be Bright und Apple Tree

```html
<!DOCTYPE html>
<html lang="de">
<head>
<meta charset="utf-8">
<title>Visitenkarte – Sanft-und-Nah Stillberatung</title>
<link href="https://fonts.googleapis.com/css2?family=Caveat:wght@500&family=Quicksand:wght@400&display=swap" rel="stylesheet">
<style>
  :root {
    --paper: #ffffff;
    --frame: #3a3a3a;
    --card: #7d8b80;
    --accent: #e0589a;
    --ink-light: #dde1db;
    --font-script: "Caveat", cursive;
    --font-text: "Quicksand", sans-serif;
  }
  * { box-sizing: border-box; margin: 0; padding: 0; }
  html, body { width: 1200px; height: 544px; overflow: hidden; background: var(--paper); }
  .sheet {
    position: relative;
    width: 1200px; height: 544px;
    border: 1.5px solid var(--frame);
    background: var(--paper);
  }
  .card {
    position: absolute;
    top: 65px;
    width: 534px; height: 346px;
    background: var(--card);
    color: var(--ink-light);
    font-family: var(--font-text);
  }
  .card--front { left: 47px; }
  .card--back { left: 612px; }

  /* Front */
  .brand-name {
    position: absolute;
    left: 0; right: 0; top: 218px;
    text-align: center;
    font-family: var(--font-text);
    font-weight: 400;
    font-size: 56px;
    line-height: 1;
    color: var(--accent);
  }
  .brand-tagline {
    position: absolute;
    left: 0; right: 0; top: 284px;
    text-align: center;
    font-size: 17px;
    letter-spacing: 0.3px;
  }

  /* Back */
  .person-name {
    position: absolute;
    left: 46px; top: 30px;
    font-family: var(--font-script);
    font-weight: 500;
    font-size: 50px;
    line-height: 1;
    color: var(--accent);
  }
  .person-role {
    position: absolute;
    left: 50px; top: 98px;
    font-size: 15px;
    line-height: 22px;
  }
  .contact-address,
  .contact-reach {
    position: absolute;
    left: 42px;
    font-size: 16px;
    line-height: 23px;
  }
  .contact-address { top: 150px; }
  .contact-reach { top: 216px; }
  .web-address {
    position: absolute;
    left: 0; right: 0; top: 280px;
    text-align: center;
    font-family: var(--font-script);
    font-weight: 500;
    font-size: 34px;
    line-height: 1;
    color: var(--accent);
  }
</style>
</head>
<body>
<div class="sheet">
  <section class="card card--front">
    <div class="brand-name">Sanft-und-Nah</div>
    <div class="brand-tagline">Stillberatung für Regensburg</div>
  </section>

  <section class="card card--back">
    <div class="person-name">Lena Marwitz</div>
    <div class="person-role">
      Fachkrankenschwester<br>
      Still- &amp; Laktationsberaterin ZMRPT
    </div>
    <div class="contact-address">
      Am Lindenweg 12<br>
      93077 Birkental
    </div>
    <div class="contact-reach">
      Telefon: 09401 5550182<br>
      E-Mail: lena@sanft-und-nah.de
    </div>
    <div class="web-address">www.sanft-und-nah.de</div>
  </section>
</div>
</body>
</html>
```